New Software Development Firm Needs Business Cards!

We just completed a successful logo design project on MockupHive and need to develop a business card design using that shiny new logo. We want a clean, modern design that communicates professionalism and tech savvy without being cliche'.

The company is "Brevant Works, LLC", but our dba is "Brevant" The business card address should reflect the full company name in the address. The logo just uses "Brevant".

Photoshop or Illustrator source files will be required, along with exact font name(s) and source(s) used.

The design will need to work well with our letterhead as well. I'm also launching a project right now for letterhead and envelopes as well. Please submit to both projects! We're excited to see the designs. Thanks...

Target Market(s)

Small to medium business professionals

Industry/Entity Type

Business

Requirements
Must have
• Need place for:
- Company name and address (5 lines)
- Phone: (1 number)
- Fax: (1 number)
- Employee's name
- Employee's position
- Employee's email address
- Company web site URL
Nice to have
• Probably want a white card, but we're open to options.

```html
<!DOCTYPE html>
<html lang="en">
<head>
<meta charset="UTF-8">
<title>Brevant – Business Cards</title>
<link href="https://fonts.googleapis.com/css2?family=Saira:wght@400;500;600&display=swap" rel="stylesheet">
<style>
  :root {
    --backdrop: #2a2a2a;
    --card-white: #ffffff;
    --card-black: #121212;
    --ink: #1a1a1a;
    --accent: #e3262b;
    --muted: #333333;
  }
  * { margin: 0; padding: 0; box-sizing: border-box; }
  html, body {
    width: 1200px; height: 900px; overflow: hidden;
    background: var(--backdrop);
    font-family: "Saira", Arial, sans-serif;
  }
  .stage { position: relative; width: 1200px; height: 900px; }
  .card {
    position: absolute; width: 580px; height: 331px;
    box-shadow: 0 14px 34px rgba(0,0,0,0.55);
  }
  .card--front { left: 90px; top: 110px; background: var(--card-white); color: var(--ink); }
  .card--back { left: 530px; top: 470px; background: var(--card-black); }

  .wordmark { font-weight: 500; letter-spacing: 1px; line-height: 1; }
  .card--front .wordmark { position: absolute; left: 34px; top: 92px; font-size: 76px; color: var(--ink); }
  .card--back .wordmark { position: absolute; left: 0; right: 0; top: 118px; text-align: center; font-size: 80px; color: #fff; }

  .divider { position: absolute; left: 34px; right: 0; top: 192px; height: 1px; background: var(--accent); }

  .holder { position: absolute; right: 28px; top: 128px; text-align: right; }
  .holder__name { color: var(--accent); font-size: 21px; font-weight: 400; line-height: 1.1; }
  .holder__role { font-size: 11px; color: var(--muted); margin-top: 4px; }

  .contacts { position: absolute; left: 350px; top: 204px; font-size: 12px; color: var(--muted); list-style: none; }
  .contacts li { display: flex; align-items: center; gap: 7px; height: 17px; }
  .contacts li.gap { margin-top: 12px; }
  .contacts svg { width: 10px; height: 10px; fill: var(--accent); flex: none; }

  .address { position: absolute; left: 34px; top: 222px; font-size: 13px; line-height: 18px; color: var(--muted); font-style: normal; }
  .address__company { color: var(--accent); font-size: 15px; margin-bottom: 2px; }

  .card--back .site { position: absolute; left: 0; right: 0; top: 226px; text-align: center; color: var(--accent); font-size: 15px; letter-spacing: 4px; }
</style>
</head>
<body>
<main class="stage">
  <section class="card card--front">
    <div class="wordmark">Brevant</div>
    <div class="holder">
      <div class="holder__name">Maren Castell</div>
      <div class="holder__role">General Manager</div>
    </div>
    <div class="divider"></div>
    <ul class="contacts">
      <li><svg viewBox="0 0 10 10"><path d="M2 0h2l1 3-1.5 1a6 6 0 0 0 2.5 2.5L7 5l3 1v2c0 1-1 2-2 2C4 10 0 6 0 2 0 1 1 0 2 0z"/></svg>+ 0 555 014 277</li>
      <li><svg viewBox="0 0 10 10"><rect x="2" y="0" width="6" height="3"/><rect x="0" y="4" width="10" height="4" rx="1"/><rect x="2" y="7" width="6" height="3"/></svg>+ 0 555 014 278</li>
      <li class="gap"><svg viewBox="0 0 10 10"><rect x="0" y="1" width="10" height="8" rx="1"/><path d="M0 2l5 4 5-4" stroke="#fff" stroke-width="1" fill="none"/></svg>info@brevantworksllc.com</li>
      <li><svg viewBox="0 0 10 10"><circle cx="5" cy="5" r="5"/><path d="M0 5h10M5 0c-3 3-3 7 0 10M5 0c3 3 3 7 0 10" stroke="#fff" stroke-width="0.8" fill="none"/></svg>www.brevantworksllc.com</li>
    </ul>
    <address class="address">
      <div class="address__company">Brevant Works, LLC</div>
      <div>Suite 48 Rd. 5106</div>
      <div>Harrowfield NV 40718 MERIDALE</div>
      <div>Suite 48 Rd. 5106</div>
      <div>Harrowfield NV 40718</div>
    </address>
  </section>

  <section class="card card--back">
    <div class="wordmark">Brevant</div>
    <div class="site">www.brevantworksllc.com</div>
  </section>
</main>
</body>
</html>
```